UK garage/funky house night flier

I need a flier design to upload to my facebook event page and also some printed fliers to promote the event.

Event is in an urban area underneath railway arches so would like a flier to reflect this with an urban background.
Updates

new photos uploaded to be used as possible backgrounds

Target Market(s)

aged 18-30

Industry/Entity Type

House

Requirements
Must have
• The following text on front of flier:

MIDNIGHT KREST PROMOTIONS PRESENTS A NIGHT CALLED…

‘COPPER TUNNEL RHYTHMZ’

Saturday 7th September 2013

@ Dock27, Marlow Lane, Digbeth, Birmingham B7 3QX

9pm till late

DJ’s playing a selection of Funky house/deep house/future garage and old school 2-step garage

(On back of flier......)

Come and enjoy yourself in a friendly, safe environment with like-minded people who are out to have a good time and rave till the early hours. This venue is part outdoor terrace and part indoor with music being played on the Sonorix-Max Soundsystem – so you know it is a night not to be missed!!

This event is guestlist only. Those not on the guest list will not be allowed entry. To get yourself on the guest list go to the facebook page www.socialpagehub.example/midnightkrestpromotions and join the event ‘Copper Tunnel Rhythmz’

Dresscode: smart. No trainers/tracksuits
Admission fee on the door is £5
Last entry: midnight
Nice to have
• must be portrait, A5 or A6 size

Urban background, maybe at night, a street with old brickwork, maybe some speakers in the foreground.

dock27 logo bottom right

Back of flier to have the map of Dock27

```html
<!DOCTYPE html>
<html lang="en">
<head>
<meta charset="utf-8">
<title>Copper Tunnel Rhythmz – Flier</title>
<link rel="stylesheet" href="https://fonts.googleapis.com/css2?family=Orbitron:wght@500&family=Comfortaa:wght@500&family=Noto+Serif:ital@1&family=Bungee&display=swap">
<style>
  :root {
    --black: #000000;
    --yellow: #e8f03a;
    --white: #ffffff;
    --brick-dark: #3a1a16;
    --brick: #7a2e24;
    --brick-light: #96443a;
    --ground: #4c4a47;
    --ground-dark: #262524;
    --title-blue: #5aa6e6;
    --title-edge: #d9ef2e;
    --logo-bg: #d8d8d8;
    --logo-ink: #2a2a2a;
  }
  * { margin: 0; padding: 0; box-sizing: border-box; }
  html, body { width: 846px; height: 1200px; overflow: hidden; background: var(--black); }
  .flier {
    position: relative;
    width: 846px;
    height: 1200px;
    background: var(--black);
    overflow: hidden;
  }
  .scene {
    position: absolute;
    left: 0; top: 0;
    width: 846px; height: 930px;
    background:
      linear-gradient(to bottom, rgba(0,0,0,0) 85%, var(--black) 100%),
      linear-gradient(to bottom, var(--brick-dark) 0%, var(--brick) 30%, var(--brick-light) 55%, var(--brick) 74%, var(--ground) 77%, var(--ground-dark) 100%);
  }
  .presenter {
    position: absolute;
    left: 0; top: 50px;
    width: 100%;
    text-align: center;
    font-family: "Orbitron", sans-serif;
    font-weight: 500;
    font-size: 30px;
    line-height: 42px;
    letter-spacing: 5px;
    color: var(--yellow);
  }
  .title {
    position: absolute;
    left: 0; top: 246px;
    width: 100%;
    text-align: center;
    font-family: "Bungee", sans-serif;
    font-weight: 400;
    color: var(--title-blue);
    -webkit-text-stroke: 5px var(--title-edge);
    paint-order: stroke fill;
  }
  .title-line { display: block; }
  .title-line--first { font-size: 96px; line-height: 118px; letter-spacing: 4px; }
  .title-line--second { font-size: 112px; line-height: 128px; letter-spacing: 6px; }
  .title-line--third { font-size: 90px; line-height: 120px; letter-spacing: 2px; }
  .lineup {
    position: absolute;
    left: 0; top: 922px;
    width: 100%;
    text-align: center;
    font-family: "Comfortaa", sans-serif;
    font-weight: 500;
    font-size: 21px;
    line-height: 36px;
    color: var(--white);
  }
  .details {
    position: absolute;
    left: 0; top: 993px;
    width: 100%;
    text-align: center;
    font-family: "Noto Serif", serif;
    font-style: italic;
    font-size: 22px;
    line-height: 38px;
    color: var(--yellow);
  }
  .venue-logo {
    position: absolute;
    left: 582px; top: 1074px;
    width: 198px; height: 72px;
    background: var(--logo-bg);
    border-radius: 4px;
    display: flex;
    align-items: center;
    justify-content: center;
    font-family: "Comfortaa", sans-serif;
    font-weight: 500;
    font-size: 28px;
    color: var(--logo-ink);
  }
</style>
</head>
<body>
  <main class="flier">
    <div class="scene" role="img" aria-label="Photograph of a red brick wall under railway arches with blue music notes and an empty wooden bench on a pavement"></div>

    <header class="presenter">
      MIDNIGHT KREST PROMOTIONS<br>
      PRESENTs<br>
      A NIGHT CALLED...
    </header>

    <h1 class="title">
      <span class="title-line title-line--first">COPPER</span>
      <span class="title-line title-line--second">TUNNEL</span>
      <span class="title-line title-line--third">RHYTHMZ</span>
    </h1>

    <p class="lineup">
      DJ's playing a selection of Funky house/deep<br>
      house/future garage and old school 2-step garage
    </p>

    <p class="details">
      Saturday 7th September 2013<br>
      @ Dock27, Marlow Lane, Digbeth, Birmingham B7 3QX<br>
      9pm till late
    </p>

    <div class="venue-logo">DOCK27</div>
  </main>
</body>
</html>
```